Harrowgate Supply Group Business Card Design

The Business Card will be one side only with Harrowgate Supplies Group Logo
Card should have:
Name
Title
Office phone Number
Cell Number
email address
Website
Street Address
Our Slogan is Strong and Steady
Looking for something that stands out from other business cards

Target Market(s)

Heavy equipment Lease Company

```html
<!DOCTYPE html>
<html lang="en">
<head>
<meta charset="utf-8">
<title>Harrowgate Supplies Group – Business Card</title>
<link rel="stylesheet" href="https://fonts.googleapis.com/css2?family=Cinzel:wght@400&family=Open+Sans:wght@400;700&display=swap">
<style>
  :root {
    --brand-red: #cf1230;
    --brand-navy: #272a77;
    --paper: #ffffff;
    --ink-grey: #4a4a4a;
    --backdrop: #d9d9dc;
  }
  * { box-sizing: border-box; margin: 0; padding: 0; }
  html, body { width: 1200px; height: 1200px; overflow: hidden; }
  body {
    background: var(--backdrop);
    font-family: "Open Sans", sans-serif;
    position: relative;
  }
  .card {
    position: absolute;
    left: 170px;
    width: 860px;
    height: 491px;
    background: var(--paper);
    box-shadow: 0 10px 30px rgba(0,0,0,0.25);
    overflow: hidden;
  }
  .card--front { top: 70px; }
  .card--back { top: 630px; }

  .band {
    position: absolute;
    left: 0; right: 0; bottom: 0;
    background: var(--brand-red);
  }
  .card--front .band { height: 170px; display: flex; align-items: center; justify-content: center; }
  .card--back .band { height: 175px; }

  .brand {
    position: absolute;
    display: flex;
    align-items: center;
    gap: 16px;
    white-space: nowrap;
  }
  .brand__dot {
    width: 60px; height: 60px;
    border-radius: 50%;
    background: var(--brand-navy);
    flex: none;
  }
  .brand__name {
    font-weight: 700;
    font-size: 32px;
    color: var(--brand-red);
    text-transform: uppercase;
    letter-spacing: 0.5px;
    line-height: 1;
  }
  .card--front .brand { left: 120px; top: 130px; }
  .card--back .brand { left: 220px; top: 60px; }

  .website {
    position: absolute;
    right: 120px;
    top: 265px;
    font-size: 17px;
    color: var(--ink-grey);
  }
  .website__domain { color: var(--brand-red); }

  .slogan {
    color: var(--paper);
    font-size: 22px;
    letter-spacing: 12px;
    text-transform: uppercase;
  }

  .rule {
    position: absolute;
    left: 0; right: 0;
    top: 232px;
    height: 2px;
    background: var(--brand-red);
  }
  .person {
    position: absolute;
    left: 90px;
    top: 202px;
    background: var(--paper);
    padding: 0 16px;
  }
  .person__name {
    font-family: "Cinzel", serif;
    font-size: 44px;
    color: var(--brand-red);
    line-height: 1.1;
  }
  .person__title {
    font-size: 19px;
    color: var(--ink-grey);
    padding-left: 30px;
  }

  .address {
    position: absolute;
    left: 90px;
    bottom: 45px;
    display: flex;
    gap: 10px;
    color: var(--paper);
    font-size: 18px;
    line-height: 1.4;
  }
  .address svg { margin-top: 4px; flex: none; }

  .contacts {
    position: absolute;
    right: 50px;
    top: 28px;
    list-style: none;
    color: var(--paper);
    font-size: 18px;
    text-align: right;
    line-height: 1.5;
  }
  .contacts li { display: flex; align-items: center; justify-content: flex-end; gap: 8px; }
  .contacts svg { flex: none; }
</style>
</head>
<body>

<section class="card card--front" aria-label="Business card front">
  <div class="brand">
    <span class="brand__dot"></span>
    <span class="brand__name">Harrowgate Supplies Group</span>
  </div>
  <p class="website">www.<span class="website__domain">harrowgatesupply</span>.com</p>
  <div class="band">
    <p class="slogan">Strong and Steady</p>
  </div>
</section>

<section class="card card--back" aria-label="Business card back">
  <div class="brand">
    <span class="brand__dot"></span>
    <span class="brand__name">Harrowgate Supplies Group</span>
  </div>
  <div class="rule"></div>
  <div class="person">
    <p class="person__name">JOHN DOE</p>
    <p class="person__title">Director</p>
  </div>
  <div class="band">
    <ul class="contacts">
      <li>1-234-567890
        <svg width="16" height="16" viewBox="0 0 16 16" aria-hidden="true"><path d="M2 6c0-3 12-3 12 0v1h-3V5.5C9 5 7 5 5 5.5V7H2z M4 8h8l1 6H3z" fill="#fff"/></svg>
      </li>
      <li>1-234-567890
        <svg width="16" height="16" viewBox="0 0 16 16" aria-hidden="true"><rect x="4" y="1" width="8" height="14" rx="1.5" fill="none" stroke="#fff" stroke-width="1.5"/><rect x="7" y="12" width="2" height="1.5" fill="#fff"/></svg>
      </li>
      <li>john@harrowgatesupply.com
        <svg width="16" height="16" viewBox="0 0 16 16" aria-hidden="true"><rect x="1" y="3" width="14" height="10" fill="#fff"/><path d="M1 3l7 6 7-6" fill="none" stroke="#cf1230" stroke-width="1.2"/></svg>
      </li>
    </ul>
    <div class="address">
      <svg width="14" height="18" viewBox="0 0 14 18" aria-hidden="true"><path d="M7 0a7 7 0 0 1 7 7c0 5-7 11-7 11S0 12 0 7a7 7 0 0 1 7-7z" fill="#fff"/><circle cx="7" cy="7" r="2.5" fill="#cf1230"/></svg>
      <p>Dummy city<br>Dummy Country Land</p>
    </div>
  </div>
</section>

</body>
</html>
```